Harbor Geriatric care need Business card design

Simple and elegance looking business card (colour choice will be very important)
Harbor geriatric care is medical consultation service for elderly population.

1st side---business logo and the doctor name/tile
eg: dr. XXX
MBBS,FRACP etc
Main room:
suite xxx AAA medical centre 18 XXX road Vic 3000
Phone:
Fax:

2nd side --different clinic address (up to 3 addresses) and need to have appointment time/ date

Suite xxx AAA medical centre , 18 XXX road VIC 3000

Please see attachment for business logo

Important: need to be compatible with Marlo Press for printing purpose.

Thank you.

hi, please look at the sample business card and create something similar. Company name: Harbor Geriatric Care PTY LTD ABN 47690518 ( all small font and no need to be obvious) company logo need to be obvious Apart from steady in support, also add Geriatrician for Community and Residential Care. Main room Dunova Medical Centre suite 2.14 204-206 Pelling street Box Hill Vic All appointment and enquiries: tel: 947160258 Fasmile: www.qwxplomz.com.au Kellwyn Medical Centre 42 dunmore road kellwyn VIC Ridgefield Care Frankston 587 Pellham road , franskton VIC 3199 Orchard Private Hospital specialist room 264 Tollard Road, Mt. Orchard VIC 3333 Dr. PN 80917kt DR. HW r8026179mm DR. GT 907612mm Thank you

```html
<!DOCTYPE html>
<html lang="en">
<head>
<meta charset="utf-8">
<title>Harbor Geriatric Care – Business Card</title>
<link rel="stylesheet" href="https://fonts.googleapis.com/css2?family=Caladea:wght@400;700&family=Open+Sans:ital,wght@0,400;0,600;1,400&display=swap">
<style>
  :root {
    --navy: #1f2a5c;
    --red: #d0202a;
    --grey: #8a8a8a;
    --card: #ffffff;
    --page: #e9e9e9;
  }
  * { margin: 0; padding: 0; box-sizing: border-box; }
  html, body { width: 1200px; height: 960px; overflow: hidden; }
  body {
    background: var(--page);
    position: relative;
    font-family: "Open Sans", Arial, sans-serif;
    color: var(--navy);
  }
  h1, h2, p { font-weight: 400; }
  .card {
    position: absolute;
    left: 270px;
    width: 660px;
    height: 372px;
    background: var(--card);
    box-shadow: 0 2px 8px rgba(0,0,0,0.18);
    overflow: hidden;
  }
  .card--appointment { top: 84px; }
  .card--contact { top: 500px; }
  .abs { position: absolute; white-space: nowrap; }

  /* Appointment side */
  .brand-title {
    left: 0; width: 100%; top: 96px; text-align: center;
    font-family: "Caladea", Georgia, serif; font-size: 37px; color: var(--navy);
  }
  .clinic { font-size: 16px; line-height: 18px; color: var(--navy); }
  .clinic--left { left: 54px; top: 168px; }
  .clinic--right { left: 314px; top: 168px; }
  .clinic-divider {
    left: 302px; top: 168px; width: 2px; height: 54px; background: var(--red);
  }
  .appointment-heading {
    left: 0; width: 100%; top: 258px; text-align: center;
    font-style: italic; font-size: 19px; letter-spacing: 0.5px; color: var(--navy);
  }
  .appointment-fields {
    left: 0; width: 100%; top: 296px; text-align: center;
    font-size: 15px; color: var(--red);
  }
  .appointment-fields span { margin: 0 8px; }

  /* Contact side */
  .brand-mark {
    left: 50px; top: 58px; width: 52px; height: 52px; border-radius: 50%;
    background: var(--red);
  }
  .brand-name {
    left: 118px; top: 60px;
    font-family: "Caladea", Georgia, serif; font-size: 37px; color: var(--navy);
  }
  .brand-tagline {
    left: 176px; top: 103px; font-size: 11px; letter-spacing: 6px;
    color: var(--grey); text-transform: uppercase;
  }
  .doctor { left: 52px; top: 140px; font-size: 15px; line-height: 20px; }
  .doctor-name { font-family: "Caladea", Georgia, serif; font-weight: 700; font-size: 17px; }
  .enquiries-label { left: 54px; top: 213px; font-size: 15px; }
  .contact-list { left: 52px; top: 249px; font-size: 15px; line-height: 21px; }
  .contact-list .key { color: var(--red); }
  .contact-list .web { color: var(--red); }
  .contact-divider {
    left: 346px; top: 240px; width: 2px; height: 94px; background: var(--red);
  }
  .main-room { left: 420px; top: 232px; font-size: 15px; line-height: 20px; }
  .main-room .label { color: var(--red); }
  .band { top: 356px; height: 16px; }
  .band--red { left: 0; width: 344px; background: var(--red); }
  .band--navy { left: 347px; right: 0; background: var(--navy); }
</style>
</head>
<body>

<section class="card card--appointment">
  <h1 class="abs brand-title">Harbor Geriatric Care</h1>
  <p class="abs clinic clinic--left">Kellwyn Medical Centre,<br>42 Dunmore Rd,<br>Kellwyn VIC 3571</p>
  <div class="abs clinic-divider"></div>
  <p class="abs clinic clinic--right">Orchard Private Hospital<br>consulting suites, 264 Tollard Rd,<br>Mt. Orchard VIC 3333</p>
  <h2 class="abs appointment-heading">NEXT APPOINTMENT</h2>
  <p class="abs appointment-fields">
    <span>Day ...............</span><span>Date .................</span><span>Time ...............Am | Pm</span>
  </p>
</section>

<section class="card card--contact">
  <div class="abs brand-mark"></div>
  <h1 class="abs brand-name">Harbor Geriatric Care</h1>
  <p class="abs brand-tagline">Steady in support</p>
  <div class="abs doctor">
    <p class="doctor-name">Dr. Pei Wen (Peter) Nair</p>
    <p>Consultant Physician and Geriatrician</p>
    <p>MBBS, FRACP, Clin Dip Pall Med.</p>
  </div>
  <p class="abs enquiries-label">All Appointments and Enquiries</p>
  <div class="abs contact-list">
    <p><span class="key">P:</span> (03) 9471 6025</p>
    <p><span class="key">F:</span> (03) 8140 2259</p>
    <p><span class="key">E:</span> info@harborgc.com.au</p>
    <p class="web">www.harborgc.com.au</p>
  </div>
  <div class="abs contact-divider"></div>
  <div class="abs main-room">
    <p class="label">Main room</p>
    <p>Suite 2.14</p>
    <p>Dunova Medical centre</p>
    <p>204-206 Pelling Street</p>
    <p>Brenholt VIC 3619</p>
  </div>
  <div class="abs band band--red"></div>
  <div class="abs band band--navy"></div>
</section>

</body>
</html>
```